Pediatric Speech Therapy Private Practice Announcement

I opened a solo private practice as a pediatric speech therapist in June 2014 in Orinda, CA in June 2014. I have 25 years experience in the field and worked as the Director of a very successful group practice of speech therapists in nearby Walnut Creek. I am trying to get my own name established in the local community and letting people know that I now have my own practice, which I call Halvery Speech-Language Center.

I would like this postcard to advertise low-cost speech-language screenings offered to nearby preschools.

Target Market(s)

Preschool Directors

Industry/Entity Type

Call

Requirements
Must have
• Photos of children, preschool ages, 3-5

Bright colors to get attention

```html
<!DOCTYPE html>
<html lang="en">
<head>
<meta charset="utf-8">
<title>Halvery Speech-Language Center – Postcard</title>
<link rel="stylesheet" href="https://fonts.googleapis.com/css2?family=Poppins:ital,wght@1,800;1,900&family=Fira+Sans+Condensed:wght@600;700;800&family=Fira+Sans+Condensed:ital,wght@1,700;1,800&display=swap">
<style>
  :root {
    --page: #ffffff;
    --red: #ec3b32;
    --orange: #f05a2c;
    --purple: #7a2f8e;
    --purple-deep: #652886;
    --ribbon: #6f2a91;
    --lime: #d6e21f;
    --white: #ffffff;
    --photo-light: #eef4f6;
    --photo-teal: #7fc6d3;
  }
  * { margin: 0; padding: 0; box-sizing: border-box; }
  html, body { width: 1200px; height: 1000px; overflow: hidden; background: var(--page); }
  .canvas { position: relative; width: 1200px; height: 1000px; }

  .postcard {
    position: absolute; left: 37px; top: 37px; width: 1132px; height: 876px;
    background: linear-gradient(135deg, var(--purple) 0%, var(--purple-deep) 100%);
    box-shadow: 6px 8px 14px rgba(0,0,0,0.35);
    overflow: hidden;
  }
  .header-band {
    position: absolute; left: 0; top: 0; width: 100%; height: 195px;
    background: linear-gradient(90deg, var(--red) 0%, var(--orange) 45%, var(--red) 100%);
  }
  .ribbon { position: absolute; left: 58px; top: 0; width: 262px; height: 182px; }
  .ribbon-label {
    position: absolute; left: 58px; top: 48px; width: 262px; text-align: center;
    font-family: "Poppins", sans-serif; font-style: italic; font-weight: 900;
    font-size: 78px; line-height: 1; color: var(--white); letter-spacing: -1px;
  }
  .headline {
    position: absolute; left: 330px; top: 52px; width: 780px; text-align: center;
    font-family: "Poppins", sans-serif; font-style: italic; font-weight: 800;
    font-size: 51px; line-height: 58px; color: var(--lime);
    text-shadow: 2px 3px 4px rgba(0,0,0,0.35);
  }
  .photo-area { position: absolute; left: 0; top: 195px; width: 800px; height: 570px; }

  .practice-name {
    position: absolute; left: 760px; top: 247px; width: 342px; text-align: center;
    font-family: "Fira Sans Condensed", sans-serif; font-weight: 800;
    font-size: 31px; line-height: 38px; color: var(--white); letter-spacing: 0.5px;
  }
  .practice-intro {
    position: absolute; left: 760px; top: 368px; width: 342px; text-align: center;
    font-family: "Fira Sans Condensed", sans-serif; font-weight: 700;
    font-size: 19px; line-height: 28px; color: var(--white);
  }
  .offer-badge {
    position: absolute; left: 812px; top: 466px; width: 240px; height: 206px;
    border-radius: 50%; border: 4px solid var(--white);
    background: radial-gradient(circle at 50% 40%, #f2523c 0%, var(--red) 70%);
    box-shadow: 2px 4px 8px rgba(0,0,0,0.3);
    display: flex; flex-direction: column; align-items: center; justify-content: center;
    font-family: "Fira Sans Condensed", sans-serif; font-style: italic; font-weight: 800;
    text-shadow: 1px 2px 3px rgba(0,0,0,0.3);
  }
  .offer-badge .offer-lead { font-size: 31px; line-height: 36px; color: var(--white); }
  .offer-badge .offer-main { font-size: 39px; line-height: 44px; color: var(--lime); }
  .offer-badge .offer-price { font-size: 41px; line-height: 46px; color: var(--white); }
  .screening-note {
    position: absolute; right: 46px; top: 686px; width: 440px; text-align: right;
    font-family: "Fira Sans Condensed", sans-serif; font-weight: 700;
    font-size: 19.5px; line-height: 28px; color: var(--white);
  }
  .call-to-action {
    position: absolute; left: 0; top: 772px; width: 100%; text-align: center;
    font-family: "Poppins", sans-serif; font-style: italic; font-weight: 800;
    font-size: 31px; line-height: 36px; color: var(--lime);
    text-shadow: 2px 2px 4px rgba(0,0,0,0.35);
  }
</style>
</head>
<body>
<div class="canvas">
  <div class="postcard">
    <div class="header-band"></div>

    <svg class="ribbon" viewBox="0 0 262 182" aria-hidden="true">
      <defs>
        <radialGradient id="ribbonFill" cx="0.5" cy="0.3" r="0.8">
          <stop offset="0" stop-color="#8a3aa3"/>
          <stop offset="1" stop-color="#5e2383"/>
        </radialGradient>
      </defs>
      <path d="M0 0 H262 V182 L131 150 L0 182 Z" fill="url(#ribbonFill)"/>
    </svg>
    <div class="ribbon-label">NEW</div>

    <h1 class="headline">Pediatric Speech Therapy<br>Practice in Orinda</h1>

    <svg class="photo-area" viewBox="0 0 800 570" role="img" aria-label="Photo of four smiling preschool children in a huddle, looking down at the camera">
      <defs>
        <linearGradient id="photoFill" x1="0" y1="0" x2="1" y2="1">
          <stop offset="0" stop-color="var(--photo-teal)"/>
          <stop offset="0.45" stop-color="var(--photo-light)"/>
          <stop offset="1" stop-color="#b6d98a"/>
        </linearGradient>
      </defs>
      <path d="M0 0 H728 C775 100 780 330 665 455 C565 555 270 560 0 522 Z" fill="url(#photoFill)"/>
      <path d="M728 0 C775 100 780 330 665 455 C565 555 270 560 0 522" fill="none" stroke="var(--red)" stroke-width="7"/>
    </svg>

    <h2 class="practice-name">HALVERY<br>SPEECH-LANGUAGE<br>CENTER</h2>
    <p class="practice-intro">A new speech therapy practice<br>in Orinda owned by<br>Dana Halvery, MS, CCC-SLP</p>

    <div class="offer-badge">
      <span class="offer-lead">OFFERING</span>
      <span class="offer-main">LOW COST</span>
      <span class="offer-price">($40)</span>
    </div>

    <p class="screening-note">On site speech-language screenings at<br>preschools this Fall in the Lamorinda area</p>

    <p class="call-to-action">Call (925) 555-0142 for additional information,<br>or to schedule an on-site screening at your preschool today!</p>
  </div>
</div>
</body>
</html>
```